依頼詳細
お客様(M様)の厚意により2月16日(土)17日(日)と2月23日(土)24日(日)に完成見学会を実施することになりました。市内に配布し、建築を考えていらっしゃる方を誘致したく考えています。見学会住所は千葉県我孫子市桜ヶ丘5丁目2-11。写真の下部に 見学会場イメージ(当社施工例) と記載してください。
メーンとなる写真に関しては家族で生活を楽しんでいる(例えばバーべキュウなど)ものが良いと考えているのですが残念ながら弊社には無いので無料画像などが利用出来ればお願い致します。弊社HPをご覧頂き利用できるデータがあれば送付致します。
記載項目
森光ハウス㈱ 04-3920-6817 http://www.kt-house.example.jp
サイズ
B4
ページ数
片面
希望イメージ
• +5 0 +5
• シンプル
複雑
• 単色
カラフル
• 暗い
明るい
• 日常
高級
• 遊び心
厳粛
• 未来的
伝統的
• 女性的
男性的
希望する色
赤系、茶系、緑系、グレー系
納品ファイル
• 高解像度JPG (.jpg)
• イラストレーター形式 (.ai)
• フォトショップ形式 (.psd)
• PNG形式 (.png)
補足説明
依頼公開後の追記内容
アウトライン済みのロゴを追加で添付致しました。
お施主宅の実際のイメージパースを追加しました。
お施主様の希望は1.家事がしやすい 2.掃除がしやすい 3.収納量が多く散らからない 4.庭でBBQや食事 5.ストレスフリー 6.お風呂からからの眺めと出入り等でした。
弊社HPでのイベント情報ですのでご覧になってください。https://kt-house-news.example.com/2019/01/583920417.html

家族の上質で楽しい暮らしを注文住宅で叶えたいという方にアピール出来ていると感じました。

皆さんの提案が良いものばかりだったので選定するのに苦労いたしました。
誠にありがとうございました。

```html
<!DOCTYPE html>
<html lang="ja">
<head>
<meta charset="utf-8">
<title>注文住宅 完成見学会｜森光ハウス</title>
<link rel="stylesheet" href="https://fonts.googleapis.com/css2?family=Noto+Sans+JP:wght@400;500;700;900&family=Noto+Serif+JP:wght@500;700&family=Great+Vibes&display=swap">
<style>
  :root {
    --green: #5e9a3c;
    --green-dark: #3f7a2a;
    --brown: #7d4e2a;
    --brown-light: #a9774b;
    --red: #b5473a;
    --paper: #ffffff;
    --ink: #3a3330;
    --muted: #7b736d;
    --line: #d9d2c9;
  }
  * { box-sizing: border-box; margin: 0; padding: 0; }
  html, body { width: 846px; height: 1200px; overflow: hidden; background: var(--paper); }
  body { font-family: "Noto Sans JP", sans-serif; color: var(--ink); }
  .flyer { position: relative; width: 846px; height: 1200px; overflow: hidden; background: var(--paper); }

  /* hero */
  .hero-photo {
    position: absolute; left: 0; top: 0; width: 846px; height: 540px;
    background: linear-gradient(120deg, #7f9a62 0%, #b7c79a 30%, #e9e4d6 55%, #c9b49a 80%, #8f7a62 100%);
  }
  .award { position: absolute; left: 22px; top: 20px; display: flex; align-items: center; gap: 8px; }
  .award-badge { width: 26px; height: 26px; border-radius: 50%; background: var(--green); }
  .award-label { font-size: 15px; font-weight: 700; color: var(--paper); }
  .catch { position: absolute; left: 180px; top: 36px; }
  .catch span {
    display: block; width: max-content; background: var(--paper); color: var(--green);
    font-weight: 900; font-size: 27px; letter-spacing: 2px; padding: 4px 12px; margin-bottom: 6px;
  }
  .catch span:nth-child(2) { margin-left: 24px; }
  .smile { position: absolute; left: 168px; top: 318px; font-family: "Great Vibes", cursive; font-size: 66px; color: var(--paper); }
  .hero-title {
    position: absolute; left: 172px; top: 398px; font-family: "Noto Serif JP", serif; font-weight: 700;
    color: var(--paper); font-size: 38px; line-height: 1.4; letter-spacing: 2px;
  }
  .hero-note { position: absolute; right: 14px; top: 518px; font-size: 11px; color: var(--paper); }

  /* left column */
  .interior-photo {
    position: absolute; left: 0; top: 540px; width: 330px; height: 500px;
    background: linear-gradient(180deg, #f3ece2 0%, #e2d2bb 45%, #c7a784 100%);
  }
  .interior-copy {
    position: absolute; left: 168px; top: 566px; writing-mode: vertical-rl;
    font-size: 14px; line-height: 1.9; color: var(--ink); height: 240px;
  }
  .features { position: absolute; left: 22px; top: 752px; width: 200px; height: 220px; list-style: none; }
  .feature {
    position: absolute; width: 92px; height: 92px; border-radius: 50%;
    background: var(--green); color: var(--paper); display: flex; align-items: center; justify-content: center;
    text-align: center; font-weight: 700; font-size: 15px; line-height: 1.3; border: 3px solid var(--paper);
  }
  .f1 { left: 52px; top: 0; }
  .f2 { left: 0; top: 62px; }
  .f3 { left: 104px; top: 62px; }
  .f4 { left: 52px; top: 124px; }

  /* event */
  .event { position: absolute; left: 338px; top: 548px; width: 500px; height: 156px; }
  .event-label {
    position: absolute; left: 0; top: 0; width: 172px; height: 96px; background: var(--brown);
    color: var(--paper); font-family: "Noto Serif JP", serif; font-weight: 700;
    display: flex; flex-direction: column; align-items: center; justify-content: center; line-height: 1.25;
  }
  .event-label .small { font-size: 24px; }
  .event-label .big { font-size: 30px; letter-spacing: 2px; }
  .dates { position: absolute; left: 182px; top: -2px; color: var(--brown); font-family: "Noto Serif JP", serif; font-weight: 700; }
  .date-row { font-size: 44px; line-height: 50px; letter-spacing: -1px; white-space: nowrap; }
  .day {
    display: inline-block; width: 24px; height: 24px; border-radius: 50%; font-family: "Noto Sans JP", sans-serif;
    font-size: 15px; line-height: 24px; text-align: center; color: var(--paper); vertical-align: middle; margin: 0 2px;
  }
  .sat { background: var(--green); }
  .sun { background: var(--red); }
  .event-info { position: absolute; left: 182px; top: 106px; font-size: 13px; color: var(--ink); line-height: 22px; }
  .event-info b { display: inline-block; background: var(--brown-light); color: var(--paper); font-weight: 500; font-size: 11px; line-height: 17px; padding: 0 6px; margin-right: 6px; }

  /* gallery */
  .gallery { position: absolute; left: 338px; top: 712px; width: 500px; height: 332px; }
  .ph { position: absolute; }
  .ph-a { left: 0; top: 0; width: 312px; height: 140px; background: linear-gradient(135deg, #e9dfcf, #bfa27f); }
  .ph-b { left: 0; top: 146px; width: 150px; height: 104px; background: linear-gradient(135deg, #ddd2c0, #a88d6c); }
  .ph-c { left: 156px; top: 146px; width: 156px; height: 104px; background: linear-gradient(135deg, #eae4da, #b9a58b); }
  .ph-d { left: 320px; top: 146px; width: 180px; height: 104px; background: linear-gradient(135deg, #e4ddd3, #b0a090); }
  .ph-e { left: 0; top: 256px; width: 312px; height: 76px; background: linear-gradient(135deg, #f0e9de, #c6b097); }
  .ph-f { left: 320px; top: 256px; width: 180px; height: 76px; background: linear-gradient(135deg, #e6ebde, #b9c4a8); }
  .cap { position: absolute; font-size: 11px; line-height: 1.55; color: var(--ink); }
  .cap-a { left: 320px; top: 2px; width: 176px; }
  .cap-lead {
    position: absolute; left: 320px; top: 88px; width: 180px; font-family: "Noto Serif JP", serif;
    color: var(--red); font-weight: 700; font-size: 16px; line-height: 1.4;
  }
  .tag {
    position: absolute; background: var(--red); color: var(--paper); font-size: 10px; padding: 1px 6px;
  }
  .tag-a { left: 6px; top: 118px; }
  .tag-b { left: 6px; top: 228px; }
  .tag-c { left: 162px; top: 228px; }

  /* footer */
  .health { position: absolute; left: 22px; top: 1062px; font-size: 17px; font-weight: 700; line-height: 1.6; color: var(--ink); }
  .health em { font-style: normal; color: var(--green-dark); }
  .company { position: absolute; right: 24px; top: 1058px; text-align: left; }
  .company-name { display: flex; align-items: center; gap: 8px; }
  .company-mark { width: 20px; height: 20px; background: var(--green); }
  .company-name span { font-size: 28px; font-weight: 700; color: var(--green-dark); }
  .company-tag { font-size: 11px; color: var(--muted); margin-bottom: 2px; }
  .contact { margin-top: 6px; font-size: 15px; font-weight: 700; color: var(--green-dark); }
  .url { font-size: 12px; color: var(--muted); }
  .rule { position: absolute; left: 0; bottom: 0; width: 846px; height: 14px; background: var(--green); }
</style>
</head>
<body>
<main class="flyer">

  <section class="hero">
    <div class="hero-photo" role="img" aria-label="庭で笑顔を見せる子どもと、家族がテーブルで食事を楽しむ明るい屋外の写真"></div>
    <div class="award"><span class="award-badge"></span><span class="award-label">受賞</span></div>
    <h2 class="catch"><span>おうちがたのしい</span><span>おうちがすき♪</span></h2>
    <p class="smile">Smile</p>
    <h1 class="hero-title">家族の笑顔が<br>あふれる家</h1>
    <p class="hero-note">見学会場イメージ(当社施工例)</p>
  </section>

  <section class="concept">
    <div class="interior-photo" role="img" aria-label="木の床と白い壁の明るいリビングダイニングの室内写真"></div>
    <p class="interior-copy">吹き抜けと大きな窓が光を<br>招き入れ、ゆったり過ごせる<br>家族の居場所をつくります。</p>
    <ul class="features">
      <li class="feature f1">温熱<br>性能</li>
      <li class="feature f2">自然<br>素材</li>
      <li class="feature f3">抗酸化<br>環境</li>
      <li class="feature f4">健康快適<br>設計</li>
    </ul>
  </section>

  <section class="event">
    <div class="event-label"><span class="small">注文住宅</span><span class="big">完成見学会</span></div>
    <div class="dates">
      <p class="date-row">2月16日<span class="day sat">土</span>17日<span class="day sun">日</span></p>
      <p class="date-row">2月23日<span class="day sat">土</span>24日<span class="day sun">日</span></p>
    </div>
    <p class="event-info"><b>時間</b>10:00～17:00<br><b>会場</b>千葉県我孫子市桜ヶ丘5丁目2-11</p>
  </section>

  <section class="gallery">
    <div class="ph ph-a" role="img" aria-label="大きな窓のある吹き抜けリビングの写真"></div>
    <p class="cap cap-a">家事動線を短くまとめ、毎日の片付けと掃除がぐっと楽になる間取りです。</p>
    <p class="cap-lead">フルオーダーだから叶う<br>私の理想の暮らし</p>
    <span class="tag tag-a">POINT 1 家事がしやすい</span>
    <div class="ph ph-b" role="img" aria-label="たっぷり収納のあるキッチンの写真"></div>
    <div class="ph ph-c" role="img" aria-label="庭に面した浴室の写真"></div>
    <span class="tag tag-b">POINT 2 収納</span>
    <span class="tag tag-c">POINT 3 眺め</span>
    <div class="ph ph-d" role="img" aria-label="庭でバーベキューを楽しむウッドデッキの写真"></div>
    <div class="ph ph-e" role="img" aria-label="明るい洗面室と廊下の写真"></div>
    <div class="ph ph-f" role="img" aria-label="見学会場周辺の案内地図"></div>
  </section>

  <footer>
    <p class="health">私たちは<em>[健康快適住宅基準]</em>による<br>健康配慮の家をつくります。</p>
    <div class="company">
      <p class="company-tag">健康の住まいから</p>
      <div class="company-name"><span class="company-mark"></span><span>森光ハウス</span></div>
      <p class="contact">TEL04-3920-6817</p>
      <p class="url">http://www.kt-house.example.jp</p>
    </div>
    <div class="rule"></div>
  </footer>

</main>
</body>
</html>
```